Stationary Design for Medical Distribution Company

We are a Medical Distribution Company based in Dar es salaam, Tanzania (East Africa). Our company was established in 1995 and we are a reputed and respected Pharmaceuticals and Medical Supplies company in the region.
We have just recently changed our company logo. A new company logo has just recently been selected through Pixel Harbor and we are now looking for stationary designs such as Business Cards, Letterheads, Envelopes, etc.. for our company.
We request you all to take a look at the attached new company logo and give us your best possible designs.
We would prefer to have a double sided business card. For letterheads, we are open to your ideas/designs.
We are looking forward for your designs!
Updates
Company details to be incorporated in designs:
Company Name: KOVEL PHARMACEUTICALS LIMITED
Company Address: Office # 42, Tumaini Works Ltd., Msasani Lane, Dar es salaam, Tanzania
Tel: +255 22 2917348 / 49, Fax: +255 22 2917350
Email: info@kovelmedix.example
Website: www.kovelmedix.example
Also should include Cell number +255 XXX XXX XXX
Name and Designation.....
Target Market(s)
Medical Sector
Industry/Entity Type
Medical
Look and feel

```html
<!DOCTYPE html>
<html lang="en">
<head>
<meta charset="utf-8">
<title>Kovel Pharmaceuticals Limited – Stationery</title>
<link rel="stylesheet" href="https://fonts.googleapis.com/css2?family=Open+Sans:wght@400;600;700&display=swap">
<style>
  :root {
    --red: #ec1c24;
    --red-soft: #f04b3c;
    --ink: #2b2b2b;
    --ink-dark: #1f1f1f;
    --grey-text: #555;
    --paper: #ffffff;
    --pattern: #e6e6e6;
    --backdrop: #6b6b6b;
  }
  * { box-sizing: border-box; margin: 0; padding: 0; }
  html, body { width: 1200px; height: 900px; overflow: hidden; }
  body {
    background: var(--backdrop);
    font-family: "Open Sans", Arial, sans-serif;
    color: var(--ink);
    position: relative;
  }
  .sheet { position: absolute; background: var(--paper); box-shadow: 0 3px 10px rgba(0,0,0,.25); }

  /* brand lockup */
  .brand { display: flex; align-items: center; gap: 6px; }
  .brand-square { background: var(--red); border-radius: 3px; flex: none; }
  .brand-name { font-weight: 700; line-height: 1.05; color: var(--ink); }
  .brand-name.light { color: #fff; }

  /* icons and contact lines */
  .icon { width: 9px; height: 9px; fill: var(--red); flex: none; }
  .contact-line { display: flex; align-items: center; gap: 4px; white-space: nowrap; }
  .contact-line.wrap { white-space: normal; align-items: flex-start; }
  .contact-line.wrap .icon { margin-top: 2px; }

  /* letterhead */
  .letterhead { left: 40px; top: 50px; width: 410px; height: 580px; }
  .letterhead .brand { position: absolute; right: 36px; top: 28px; }
  .letterhead .brand-square { width: 34px; height: 34px; }
  .letterhead .brand-name { font-size: 12px; }
  .letter-body { position: absolute; left: 70px; top: 140px; width: 270px; font-size: 7.5px; line-height: 1.55; color: var(--grey-text); }
  .letter-body p { margin-bottom: 10px; text-align: justify; }
  .sign-off { margin-top: 14px; }
  .signature-space { width: 70px; height: 18px; margin: 6px 0 4px; }
  .signatory { font-weight: 600; color: var(--ink); }
  .letter-mark { position: absolute; left: 36px; bottom: 36px; width: 80px; height: 80px; background: var(--red); border-radius: 8px; display: flex; align-items: center; justify-content: center; color: #fff; font-weight: 700; font-size: 15px; }
  .letter-contacts { position: absolute; right: 36px; bottom: 40px; display: flex; align-items: flex-end; gap: 16px; font-size: 6.5px; color: var(--grey-text); line-height: 1.7; }
  .letter-contacts .address { width: 120px; }

  /* white envelope */
  .envelope { left: 480px; top: 50px; width: 660px; height: 280px; overflow: hidden; }
  .envelope .brand { position: absolute; right: 40px; top: 34px; }
  .envelope .brand-square { width: 42px; height: 42px; }
  .envelope .brand-name { font-size: 15px; }
  .envelope-contacts { position: absolute; right: 56px; bottom: 44px; display: flex; gap: 18px; font-size: 7.5px; color: var(--grey-text); line-height: 1.7; }
  .envelope-contacts > div { padding-left: 12px; border-left: 1px solid #ccc; }
  .envelope-contacts > div:first-child { border-left: 0; padding-left: 0; }
  .envelope-band { position: absolute; left: 0; right: 0; bottom: 0; height: 26px; background: var(--red); }

  /* red envelope back */
  .envelope-back { left: 480px; top: 350px; width: 660px; height: 280px; background: var(--red); overflow: hidden; }
  .envelope-flap { position: absolute; left: 0; right: 0; top: 0; height: 46px; border-bottom: 2px solid #c8141b; }
  .envelope-back-name { position: absolute; left: 150px; top: 90px; font-size: 92px; font-weight: 700; color: var(--red-soft); letter-spacing: 4px; }

  /* business cards */
  .card { top: 660px; width: 260px; height: 150px; overflow: hidden; }
  .card-blank { left: 40px; }
  .card-back-a { left: 326px; }
  .card-front { left: 612px; background: var(--ink); color: #fff; }
  .card-back-b { left: 898px; }
  .card-pattern { position: absolute; inset: 0; background: var(--pattern); }
  .card-band { position: absolute; left: 0; right: 24px; top: 52px; height: 46px; background: var(--ink-dark); padding-left: 44px; display: flex; align-items: center; }
  .card-band .brand-square { width: 28px; height: 28px; }
  .card-band .brand-name { font-size: 10.5px; }
  .card-front .name-bar { position: absolute; left: 0; top: 14px; right: 120px; height: 30px; background: var(--red); padding: 4px 0 0 56px; }
  .name-bar .person { font-size: 9px; font-weight: 700; }
  .name-bar .role { font-size: 7px; }
  .card-front .front-square { position: absolute; left: 16px; top: 54px; width: 34px; height: 34px; background: var(--red); border-radius: 3px; }
  .card-front .company { position: absolute; left: 60px; top: 56px; font-size: 8.5px; font-weight: 700; }
  .card-front .front-contacts { position: absolute; left: 150px; top: 74px; font-size: 6.5px; line-height: 1.75; }
  .card-front .front-address { position: absolute; left: 16px; top: 100px; width: 120px; font-size: 6.5px; line-height: 1.6; }
</style>
</head>
<body>
<svg width="0" height="0" style="position:absolute" aria-hidden="true">
  <defs>
    <symbol id="icon-pin" viewBox="0 0 10 10"><path d="M5 0a3.5 3.5 0 0 0-3.5 3.5C1.5 6 5 10 5 10s3.5-4 3.5-6.5A3.5 3.5 0 0 0 5 0zm0 5a1.5 1.5 0 1 1 0-3 1.5 1.5 0 0 1 0 3z"/></symbol>
    <symbol id="icon-phone" viewBox="0 0 10 10"><rect width="10" height="10" rx="2"/><path d="M3 2.2l1 1.6-.6.8c.5 1 1.1 1.6 2 2l.8-.6 1.6 1-.5 1.2C5 8 2 5 1.9 2.7z" fill="#fff"/></symbol>
    <symbol id="icon-mail" viewBox="0 0 10 10"><rect width="10" height="10" rx="2"/><path d="M2 3h6v4H2zM2 3l3 2.2L8 3" fill="none" stroke="#fff" stroke-width=".8"/></symbol>
    <symbol id="icon-web" viewBox="0 0 10 10"><rect width="10" height="10" rx="2"/><circle cx="5" cy="5" r="2.8" fill="none" stroke="#fff" stroke-width=".8"/><path d="M2.2 5h5.6M5 2.2v5.6" stroke="#fff" stroke-width=".6"/></symbol>
  </defs>
</svg>

<!-- Letterhead -->
<section class="sheet letterhead">
  <div class="brand">
    <span class="brand-square"></span>
    <span class="brand-name">Kovel<br>Pharmaceuticals<br>Limited</span>
  </div>
  <div class="letter-body">
    <p>We thank you for your continued trust in our distribution service. Our team will deliver the requested medical supplies to your facility within the agreed schedule, and each shipment will carry full quality records for your review.</p>
    <p>Please contact our office if you need any further details about pricing, stock levels or delivery times. We look forward to serving you again.</p>
    <div class="sign-off">Yours,</div>
    <div class="signature-space" role="img" aria-label="Space for handwritten signature"></div>
    <div class="signatory">Amani Mrisho</div>
    <div>Director</div>
  </div>
  <div class="letter-mark">KOVEL</div>
  <div class="letter-contacts">
    <div class="contact-line wrap address"><svg class="icon"><use href="#icon-pin"/></svg><span>Office # 42, Tumaini Works Ltd., Msasani Lane, Dar es salaam, Tanzania</span></div>
    <div>
      <div class="contact-line"><svg class="icon"><use href="#icon-phone"/></svg>+255 22 2917348 / 49</div>
      <div class="contact-line"><svg class="icon"><use href="#icon-phone"/></svg>+255 22 2917350</div>
      <div class="contact-line"><svg class="icon"><use href="#icon-mail"/></svg>info@kovelmedix.example</div>
      <div class="contact-line"><svg class="icon"><use href="#icon-web"/></svg>www.kovelmedix.example</div>
    </div>
  </div>
</section>

<!-- Envelope front -->
<section class="sheet envelope">
  <div class="brand">
    <span class="brand-square"></span>
    <span class="brand-name">Kovel<br>Pharmaceuticals<br>Limited</span>
  </div>
  <div class="envelope-contacts">
    <div class="contact-line wrap"><svg class="icon"><use href="#icon-pin"/></svg><span>Office # 42, Tumaini Works Ltd.,<br>Msasani Lane, Dar es salaam, Tanzania</span></div>
    <div>
      <div class="contact-line"><svg class="icon"><use href="#icon-phone"/></svg>+255 22 2917348 / 49</div>
      <div class="contact-line"><svg class="icon"><use href="#icon-phone"/></svg>+255 22 2917350</div>
    </div>
    <div>
      <div class="contact-line"><svg class="icon"><use href="#icon-mail"/></svg>info@kovelmedix.example</div>
      <div class="contact-line"><svg class="icon"><use href="#icon-web"/></svg>www.kovelmedix.example</div>
    </div>
  </div>
  <div class="envelope-band"></div>
</section>

<!-- Envelope back -->
<section class="sheet envelope-back">
  <div class="envelope-flap"></div>
  <div class="envelope-back-name">KOVEL</div>
</section>

<!-- Business cards -->
<section class="sheet card card-blank"></section>

<section class="sheet card card-back-a">
  <div class="card-pattern" role="img" aria-label="Light grey repeating brand pattern"></div>
  <div class="card-band brand">
    <span class="brand-square"></span>
    <span class="brand-name light">Kovel<br>Pharmaceuticals<br>Limited</span>
  </div>
</section>

<section class="sheet card card-front">
  <div class="name-bar">
    <div class="person">Amani Mrisho</div>
    <div class="role">Sales Director</div>
  </div>
  <div class="front-square"></div>
  <div class="company">Kovel Pharmaceuticals Limited</div>
  <div class="front-contacts">
    <div class="contact-line"><svg class="icon"><use href="#icon-phone"/></svg>+255 XXX XXX XXX</div>
    <div class="contact-line"><svg class="icon"><use href="#icon-phone"/></svg>+255 22 2917348 / 49</div>
    <div class="contact-line"><svg class="icon"><use href="#icon-phone"/></svg>+255 22 2917350</div>
    <div class="contact-line"><svg class="icon"><use href="#icon-mail"/></svg>info@kovelmedix.example</div>
    <div class="contact-line"><svg class="icon"><use href="#icon-web"/></svg>www.kovelmedix.example</div>
  </div>
  <div class="front-address contact-line wrap"><svg class="icon"><use href="#icon-pin"/></svg><span>Office # 42, Tumaini Works Ltd., Msasani Lane, Dar es salaam, Tanzania</span></div>
</section>

<section class="sheet card card-back-b">
  <div class="card-pattern" role="img" aria-label="Light grey repeating brand pattern"></div>
  <div class="card-band brand">
    <span class="brand-square"></span>
    <span class="brand-name light">Kovel<br>Pharmaceuticals<br>Limited</span>
  </div>
</section>
</body>
</html>
```